Financial Services Postcard Design

Glen Ostrow, CPA
Financial Services
Accounting/Tax/Consulting
Services include but not limited to
Financial Statements
Tax Returns
CFO/Controller services
Budgeting and Forecasting
Cash Management
Payroll / AP/ AR
Insurance Analysis
Cost Analysis
Special projects

I need a postcard design for my new financial service company to assist businesses in the Orange County area of southern California. I'm looking for a warm but bright look to represent CPA with many years of Management experience with manufacturing companies that can relate to business issues and provide solutions for small business.

Accounting

```html
<!DOCTYPE html>
<html lang="en">
<head>
<meta charset="utf-8">
<title>Harborline Financial Postcard</title>
<link rel="stylesheet" href="https://fonts.googleapis.com/css2?family=Heebo:wght@300;400&display=swap">
<style>
  :root {
    --orange: #f29a16;
    --dark: #1f2023;
    --dark-strip: #2a2422;
    --cream: #fbe9c8;
    --white: #ffffff;
    --stamp: #c8c8c8;
    --rule: #a9a9a9;
    --label: #6d6d6d;
    --frame: #f7d36a;
  }
  * { margin: 0; padding: 0; box-sizing: border-box; }
  html, body {
    width: 1200px; height: 1000px; overflow: hidden;
    background: var(--white);
    font-family: "Heebo", "Helvetica Neue", Arial, sans-serif;
  }
  .canvas { position: relative; width: 1200px; height: 1000px; }

  .card {
    position: absolute; left: 37px; width: 666px; height: 479px;
    overflow: hidden;
    box-shadow: 2px 3px 4px rgba(0,0,0,0.35);
  }
  .card--front { top: 15px; }
  .card--back { top: 508px; background: var(--white); }

  /* front */
  .desk-photo {
    position: absolute; inset: 0;
    background:
      radial-gradient(ellipse at 15% 15%, #8e9196 0%, rgba(142,145,150,0) 35%),
      radial-gradient(ellipse at 40% 80%, #cfd2d2 0%, rgba(207,210,210,0) 30%),
      radial-gradient(ellipse at 92% 80%, #8a1f22 0%, rgba(138,31,34,0) 22%),
      linear-gradient(135deg, #2b2c30 0%, var(--dark) 60%, #1a1b1d 100%);
  }
  .brand-band {
    position: absolute; left: 0; top: 159px; width: 100%; height: 142px;
    background: var(--orange);
  }
  .contact-strip {
    position: absolute; left: 0; top: 94px; width: 100%; height: 25px;
    background: var(--dark-strip);
  }
  .contact-line {
    position: absolute; right: 172px; top: 6px;
    font-size: 10.5px; font-weight: 300; color: #e8b45f;
    word-spacing: 1px; white-space: nowrap;
  }
  .contact-line span { margin-left: 14px; }
  .name {
    position: absolute; right: 172px; top: 22px;
    font-size: 33px; font-weight: 300; color: var(--cream);
    line-height: 1; letter-spacing: -0.3px;
  }
  .name-rule {
    position: absolute; left: 243px; top: 61px; width: 274px; height: 1px;
    background: rgba(255,240,210,0.6);
  }
  .firm {
    position: absolute; right: 172px; top: 63px;
    font-size: 20px; font-weight: 300; color: var(--cream);
    letter-spacing: 0.2px; white-space: nowrap;
  }
  .portrait {
    position: absolute; left: 519px; top: 82px; width: 112px; height: 196px;
    border: 3px solid var(--frame);
    background: linear-gradient(180deg, #e9dfb8 0%, #cdb98a 40%, #2a2a33 70%, #1d1d24 100%);
  }
  .services {
    position: absolute; top: 312px; list-style: none;
  }
  .services--left { left: 56px; }
  .services--right { left: 353px; }
  .services li {
    display: flex; align-items: center; height: 33px;
    font-size: 18px; font-weight: 300; color: var(--white);
    text-shadow: 0 1px 2px rgba(0,0,0,0.6);
    white-space: nowrap;
  }
  .services svg { width: 10px; height: 12px; margin-right: 12px; flex: none; }

  /* back */
  .brand-panel {
    position: absolute; left: 0; top: 0; width: 319px; height: 100%;
    background: var(--orange);
  }
  .papers-photo {
    position: absolute; left: 13px; top: 0; width: 296px; height: 303px;
    background: linear-gradient(150deg, #f4f4f2 0%, #e6e7e4 55%, #cfd0cc 100%);
    clip-path: polygon(28% 0, 100% 0, 100% 70%, 38% 100%, 0 60%, 10% 20%);
  }
  .firm-name {
    position: absolute; left: 0; top: 318px; width: 319px;
    text-align: center; color: var(--white);
    font-size: 40px; font-weight: 300; line-height: 1.1;
  }
  .stamp {
    position: absolute; left: 526px; top: 28px; width: 114px; height: 125px;
    background: var(--stamp);
    display: flex; justify-content: center; padding-top: 48px;
    font-size: 14px; font-weight: 300; color: #707070;
  }
  .address-lines { position: absolute; left: 346px; top: 193px; width: 293px; }
  .address-lines div { height: 33px; border-top: 1px solid var(--rule); }

  .sample-label {
    position: absolute; left: 902px; top: 473px;
    font-size: 30px; font-weight: 400; color: var(--label);
  }
</style>
</head>
<body>
<div class="canvas">

  <section class="card card--front">
    <div class="desk-photo" role="img" aria-label="Dark desk seen from above with a laptop, a notebook, a pen and a red folder"></div>

    <div class="brand-band">
      <div class="name">Glen Ostrow</div>
      <div class="name-rule"></div>
      <div class="firm">HARBORLINE FINANCIAL</div>
      <div class="contact-strip">
        <p class="contact-line">718 N Willowbend Ln. Tustin, Ca. 92780<span>714-555-0142</span><span>GlenOstrow@mailbridge.net</span></p>
      </div>
    </div>

    <div class="portrait" role="img" aria-label="Portrait photo of the accountant in a dark suit"></div>

    <ul class="services services--left">
      <li><svg viewBox="0 0 10 12"><path d="M2 1l5 5-5 5" fill="none" stroke="#fff" stroke-width="2"/></svg>Accounting</li>
      <li><svg viewBox="0 0 10 12"><path d="M2 1l5 5-5 5" fill="none" stroke="#fff" stroke-width="2"/></svg>Tax</li>
      <li><svg viewBox="0 0 10 12"><path d="M2 1l5 5-5 5" fill="none" stroke="#fff" stroke-width="2"/></svg>Consulting</li>
      <li><svg viewBox="0 0 10 12"><path d="M2 1l5 5-5 5" fill="none" stroke="#fff" stroke-width="2"/></svg>Financial Statements</li>
    </ul>
    <ul class="services services--right">
      <li><svg viewBox="0 0 10 12"><path d="M2 1l5 5-5 5" fill="none" stroke="#fff" stroke-width="2"/></svg>Tax Returns</li>
      <li><svg viewBox="0 0 10 12"><path d="M2 1l5 5-5 5" fill="none" stroke="#fff" stroke-width="2"/></svg>CfO / Controller Services</li>
      <li><svg viewBox="0 0 10 12"><path d="M2 1l5 5-5 5" fill="none" stroke="#fff" stroke-width="2"/></svg>Budgeting And Forecasting</li>
      <li><svg viewBox="0 0 10 12"><path d="M2 1l5 5-5 5" fill="none" stroke="#fff" stroke-width="2"/></svg>Cash Management</li>
    </ul>
  </section>

  <section class="card card--back">
    <div class="brand-panel">
      <div class="papers-photo" role="img" aria-label="Scattered sheets of grid paper with a black pen"></div>
      <div class="firm-name">Harborline<br>Financial</div>
    </div>
    <div class="stamp">Stamp</div>
    <div class="address-lines">
      <div></div><div></div><div></div><div></div><div></div><div></div><div></div>
    </div>
  </section>

  <p class="sample-label">sample 01</p>
</div>
</body>
</html>
```